Promotional Poster for "Bowls & Barrels" Community Event

Bowls & Barrels is a fun, high-energy annual fundraising event where guests enjoy gourmet taco creations and craft beer from some of Clark County's finest chefs and brewers. This community event is a fundraiser, supporting Hollis Ridge Food Bank in Southwest Washington. We need a 11x17" full-color event poster for our 2019 Bowls & Barrels event. For more information, visit our event website: www.bowlsandbarrels-fest.org
Target Market(s)
Poster to be displayed in breweries, restaurants, bars, and taprooms
Industry/Entity Type
Non Profit
Colors
Designer to choose colors to be used in the design.
Look and feel
Each slider illustrates characteristics of the customer's brand and the style your logo design should communicate.

```html
<!DOCTYPE html>
<html lang="en">
<head>
<meta charset="utf-8">
<title>Bowls &amp; Barrels 2019</title>
<link rel="stylesheet" href="https://fonts.googleapis.com/css2?family=Saira+Condensed:wght@700;800&family=Saira:wght@700&family=Libre+Baskerville:wght@700&display=swap">
<style>
  :root {
    --silver-light: #f2f2f2;
    --silver-mid: #c9c9c9;
    --silver-dark: #8f8f8f;
    --date-red: #ef3b2c;
    --date-orange: #f26f25;
    --band-red: #e21f26;
    --band-deep: #b8161c;
    --pill-pink: #e2265a;
    --pill-red: #e23a2a;
    --ink: #2c2c2c;
    --brand-green: #1f7a45;
    --accent-rose: #b8837a;
    --accent-gold: #cbbb4a;
    --white: #ffffff;
  }
  * { margin: 0; padding: 0; box-sizing: border-box; }
  html, body { width: 923px; height: 1200px; overflow: hidden; background: var(--white); }
  .poster {
    position: relative; width: 923px; height: 1200px; overflow: hidden;
    font-family: "Saira Condensed", "Arial Narrow", sans-serif;
    background:
      radial-gradient(ellipse 60% 35% at 50% 22%, rgba(255,255,255,.85), rgba(255,255,255,0) 70%),
      radial-gradient(ellipse 70% 40% at 50% 68%, rgba(255,255,255,.7), rgba(255,255,255,0) 70%),
      radial-gradient(ellipse 35% 25% at 5% 100%, rgba(255,255,255,.95), rgba(255,255,255,0) 70%),
      radial-gradient(ellipse 35% 25% at 95% 100%, rgba(255,255,255,.95), rgba(255,255,255,0) 70%),
      linear-gradient(180deg, var(--silver-dark) 0%, var(--silver-mid) 30%, var(--silver-mid) 70%, var(--silver-dark) 100%);
  }
  .corner-art { position: absolute; top: 0; }
  .corner-art--left {
    left: 0; width: 258px; height: 205px;
    background: linear-gradient(160deg, var(--accent-rose), rgba(184,131,122,.55));
  }
  .corner-art--right {
    right: 0; width: 217px; height: 298px;
    background: linear-gradient(200deg, var(--accent-gold), rgba(203,187,74,.55));
  }
  .brand {
    position: absolute; top: 154px; left: 0; width: 100%;
    display: flex; justify-content: center; align-items: center; gap: 12px;
  }
  .brand__dot { width: 40px; height: 40px; border-radius: 50%; background: var(--brand-green); }
  .brand__name {
    font-family: "Libre Baskerville", Georgia, serif; font-weight: 700;
    font-size: 21px; color: var(--brand-green); letter-spacing: .5px;
  }
  .dates { position: absolute; top: 208px; left: 0; width: 100%; text-align: center; }
  .dates__line {
    display: block; font-weight: 700; font-size: 58px; line-height: 57px; letter-spacing: .5px;
    background: linear-gradient(90deg, var(--date-red), var(--date-orange));
    -webkit-background-clip: text; background-clip: text; color: transparent;
  }
  .band {
    position: absolute; left: 0; top: 405px; width: 100%; height: 207px;
    background: linear-gradient(90deg, var(--band-red), var(--band-deep) 50%, var(--band-red));
    border-top: 2px solid var(--white); border-bottom: 2px solid var(--white);
    box-shadow: inset 0 6px 0 var(--band-red), inset 0 -6px 0 var(--band-red);
  }
  .badge {
    position: absolute; left: 268px; top: 333px; width: 386px; height: 332px; border-radius: 50%;
    background: radial-gradient(circle at 50% 45%, #ffffff, #e3e3e3 70%, #c5c5c5 100%);
    border: 6px solid #d9e6f2;
    box-shadow: 0 4px 14px rgba(0,0,0,.3);
    display: flex; align-items: center; justify-content: center; text-align: center;
  }
  .badge__name {
    font-weight: 800; font-size: 70px; line-height: 66px; color: var(--ink);
    text-transform: uppercase; letter-spacing: 1px;
  }
  .tickets {
    position: absolute; top: 662px; left: 0; width: 100%; text-align: center; color: var(--date-orange);
    font-family: "Saira", "Arial", sans-serif;
  }
  .tickets__line {
    display: block; font-weight: 700; font-size: 44px; line-height: 40px;
    font-variant: small-caps; letter-spacing: 2px;
  }
  .tickets__line--packs { margin-top: 8px; }
  .site-link {
    position: absolute; top: 821px; left: 262px; width: 400px; height: 38px;
    border-radius: 8px;
    background: linear-gradient(90deg, var(--pill-pink), var(--pill-red));
    box-shadow: 0 3px 6px rgba(0,0,0,.25);
    color: var(--white); font-weight: 700; font-size: 24px; line-height: 38px;
    text-align: center; text-transform: uppercase; text-decoration: none;
  }
  .features {
    position: absolute; top: 868px; left: 0; width: 100%; text-align: center; color: var(--ink);
    list-style: none; font-family: "Saira", "Arial", sans-serif;
  }
  .features__title { font-weight: 700; font-size: 22px; line-height: 30px; font-variant: small-caps; letter-spacing: 2px; }
  .features__item {
    font-weight: 700; font-size: 38px; line-height: 37px;
    font-variant: small-caps; letter-spacing: 1.5px;
  }
</style>
</head>
<body>
<main class="poster">
  <div class="corner-art corner-art--left" role="img" aria-label="Rose-copper mirrored disco ball"></div>
  <div class="corner-art corner-art--right" role="img" aria-label="Gold mirrored disco ball"></div>

  <div class="brand">
    <span class="brand__dot"></span>
    <span class="brand__name">Hollis Ridge Food Bank</span>
  </div>

  <h2 class="dates">
    <span class="dates__line">FRIDAY, MAY 3, 2019</span>
    <span class="dates__line">SATURDAY, MAY 4, 2019</span>
  </h2>

  <div class="band"></div>
  <div class="badge">
    <h1 class="badge__name">Bowls &amp;<br>Barrels</h1>
  </div>

  <div class="tickets">
    <span class="tickets__line">General Admission: $35</span>
    <span class="tickets__line">VIP Fiesta Ticket: $45</span>
    <span class="tickets__line tickets__line--packs">6-Pack Tickets Available</span>
  </div>

  <a class="site-link" href="#">www.bowlsandbarrels-fest.org</a>

  <ul class="features">
    <li class="features__title">Featuring:</li>
    <li class="features__item">12 Breweries</li>
    <li class="features__item">12 Restaurants</li>
    <li class="features__item">Desserts &amp; Beverages</li>
    <li class="features__item">Raffle Drawing</li>
    <li class="features__item">Live Music</li>
    <li class="features__item">Beer Bottle Ring Toss</li>
  </ul>
</main>
</body>
</html>
```